Energy Company needs a Business Card Design

We need a business card design for a new company based in Singapore called Tavelo Energy. Tavelo Energy is a producer of renewable energies largely for the biofuels market. Sourced entirely from sustainable resources, Tavelo Energy aims to be a fully integrated oil company operating in 100% sustainable way. We would like to see designs that use the same colours as the attached file.

Industry/Entity Type

Business

```html
<!DOCTYPE html>
<html lang="en">
<head>
<meta charset="utf-8">
<title>Tavelo Energy – Business Card</title>
<link rel="stylesheet" href="https://fonts.googleapis.com/css2?family=Open+Sans:ital,wght@0,400;0,600;1,400&family=Questrial&display=swap">
<style>
  :root {
    --backdrop: #a2a2a2;
    --backdrop-inner: #a9a9a9;
    --card-white: #ffffff;
    --card-stone: #f1f1ef;
    --leaf-green: #8abd2f;
    --silver: #bdbdbd;
    --swoosh: #c9c9c9;
    --ink: #555555;
    --ink-soft: #666666;
  }
  * { box-sizing: border-box; margin: 0; padding: 0; }
  html, body { width: 1080px; height: 1200px; overflow: hidden; }
  body {
    background: var(--backdrop);
    font-family: "Open Sans", Arial, sans-serif;
    position: relative;
  }
  .stage {
    position: absolute; inset: 36px;
    background: var(--backdrop-inner);
  }
  .card {
    position: absolute; left: 120px; width: 838px;
    box-shadow: 0 1px 3px rgba(0,0,0,.15);
    overflow: hidden;
  }
  .card--front { top: 92px; height: 480px; background: var(--card-white); }
  .card--back {
    top: 641px; height: 478px;
    background: radial-gradient(circle at 50% 40%, #f6f6f4, var(--card-stone));
  }

  .brand {
    font-family: "Questrial", "Open Sans", sans-serif;
    color: var(--silver);
    display: flex; align-items: center; white-space: nowrap;
  }
  .brand__dot { border-radius: 50%; background: var(--leaf-green); flex: none; }
  .card--front .brand { position: absolute; left: 44px; top: 60px; font-size: 38px; gap: 12px; }
  .card--front .brand__dot { width: 22px; height: 22px; }

  .identity { position: absolute; left: 513px; top: 34px; }
  .identity__name { font-size: 35px; color: var(--ink); letter-spacing: 0.5px; line-height: 1.1; }
  .identity__role { font-size: 23px; color: var(--ink-soft); margin-top: 2px; }

  .contacts { position: absolute; left: 513px; top: 136px; list-style: none; }
  .contacts__item {
    display: flex; align-items: center; height: 42px;
    font-size: 22px; letter-spacing: 0.6px; color: var(--ink);
  }
  .contacts__icon { width: 22px; height: 22px; margin-right: 14px; fill: var(--ink); flex: none; }

  .wave { position: absolute; left: 0; bottom: 0; width: 838px; height: 160px; }

  .card--back .brand {
    position: absolute; left: 0; right: 0; top: 130px;
    justify-content: center; font-size: 84px; gap: 22px;
  }
  .card--back .brand__dot { width: 34px; height: 34px; }
  .slogan {
    position: absolute; left: 0; right: 0; top: 386px; text-align: center;
    font-style: italic; font-size: 28px; color: var(--leaf-green);
  }
</style>
</head>
<body>
<div class="stage"></div>

<section class="card card--front" aria-label="Business card front">
  <div class="brand"><span class="brand__name">Tavelo Energy</span><span class="brand__dot"></span></div>

  <div class="identity">
    <p class="identity__name">XXXXXXXXXXXXX</p>
    <p class="identity__role">Managing Director</p>
  </div>

  <ul class="contacts">
    <li class="contacts__item">
      <svg class="contacts__icon" viewBox="0 0 24 24"><path d="M12 1a8 8 0 0 0-8 8c0 6 8 14 8 14s8-8 8-14a8 8 0 0 0-8-8zm0 11a3 3 0 1 1 0-6 3 3 0 0 1 0 6z"/></svg>
      XXXXXXXXXXXX
    </li>
    <li class="contacts__item">
      <svg class="contacts__icon" viewBox="0 0 24 24"><path d="M6.6 10.8a15 15 0 0 0 6.6 6.6l2.2-2.2c.3-.3.7-.4 1-.2 1.1.4 2.3.6 3.6.6.6 0 1 .4 1 1V20c0 .6-.4 1-1 1A17 17 0 0 1 3 4c0-.6.4-1 1-1h3.5c.6 0 1 .4 1 1 0 1.3.2 2.5.6 3.6.1.3 0 .7-.2 1z"/></svg>
      XXXXXXXXXXXX
    </li>
    <li class="contacts__item">
      <svg class="contacts__icon" viewBox="0 0 24 24"><path d="M7 1h10a2 2 0 0 1 2 2v18a2 2 0 0 1-2 2H7a2 2 0 0 1-2-2V3a2 2 0 0 1 2-2zm0 3v14h10V4zm5 15.5a1 1 0 1 0 0 2 1 1 0 0 0 0-2z"/></svg>
      XXXXXXXXXXXX
    </li>
    <li class="contacts__item">
      <svg class="contacts__icon" viewBox="0 0 24 24"><path d="M12 2a10 10 0 1 0 0 20 10 10 0 0 0 0-20zm6.9 6h-3a15 15 0 0 0-1.3-3.9A8 8 0 0 1 18.9 8zM12 4c.8 1.2 1.5 2.5 1.9 4h-3.8c.4-1.5 1.100-2.8 1.9-4zM4.3 14a8 8 0 0 1 0-4h3.4a16 16 0 0 0 0 4zm.8 2h3a15 15 0 0 0 1.3 3.9A8 8 0 0 1 5.1 16zm3-8h-3a8 8 0 0 1 4.3-3.9A15 15 0 0 0 8.1 8zM12 20c-.8-1.2-1.5-2.5-1.9-4h3.8c-.4 1.5-1.1 2.8-1.9 4zm2.3-6H9.7a14 14 0 0 1 0-4h4.6a14 14 0 0 1 0 4zm.3 5.9a15 15 0 0 0 1.3-3.9h3a8 8 0 0 1-4.3 3.9zm1.7-5.9a16 16 0 0 0 0-4h3.4a8 8 0 0 1 0 4z"/></svg>
      XXXXXXXXXXXX
    </li>
    <li class="contacts__item">
      <svg class="contacts__icon" viewBox="0 0 24 24"><path d="M2 5h20v14H2zm2 2v.5l8 5.5 8-5.5V7l-8 5.5z"/></svg>
      XXXXXXXXXXXX
    </li>
  </ul>

  <svg class="wave" viewBox="0 0 838 160" preserveAspectRatio="none" aria-hidden="true">
    <path d="M380 84 C560 80 720 52 838 18 L838 44 C720 68 560 90 380 88 Z" fill="var(--swoosh)"/>
    <path d="M0 76 C150 64 300 86 420 90 C600 94 740 70 838 50 L838 160 L0 160 Z" fill="var(--leaf-green)"/>
  </svg>
</section>

<section class="card card--back" aria-label="Business card back">
  <div class="brand"><span class="brand__name">Tavelo Energy</span><span class="brand__dot"></span></div>
  <p class="slogan">“xxxxxxxxxx Slogan xxxxxxxxxx”</p>
</section>
</body>
</html>
```